Guitar teacher and Composer needs a Business Card design

I am looking for a designer who would like to implement the general idea of the design which I am providing with a draft in the uploaded file called Tomas.png. Please feel free to add your own creative touch to my idea.
There should definitely be an abstract image of a guitar on the business card. The colours to use - black and white, could be also grey. Which one to use as the main colour - to your decision. You can try to make it half-half, for example black part with guitar and the rest - white or the other way round. Would be cool to see there some element standing out in red, such as some note, or one or all strings of the guitar, or the line of the contour of the guitar for example..
It would also be nice to see a "reverse" version where the background would be black and the strings and contour of the guitar would be white etc.
Thanks to everyone who is going to participate in this design project!
Target Market(s)
potential students and customers
Industry/Entity Type
Teacher
Contact Information for Business Card
see "Project description"
Requirements
Must have
- I want to have an ABSTRACT image of a CLASSICAL guitar or part of it. It can be just the contour of it or just a few lines giving a hint about it or so.
Nice to have
- Would be good to have some small element standing out in red. Like some little detail, or one line, or icons of contacts, or string(s) of the guitar, or a note.......
Should not have
- I DON'T want to have a PHOTO of a guitar on my business card. And i DON'T need an image of an E-GUITAR.
- I don't want the words "Phone", "E-Mail", "Website", or "Address" to appear on the business card but rather have icons/symbols for that, as shown in my draft.

```html
<!DOCTYPE html>
<html lang="de">
<head>
<meta charset="utf-8">
<title>Tomas Marenko – Visitenkarte</title>
<link href="https://fonts.googleapis.com/css2?family=Archivo+Black&family=Questrial&display=swap" rel="stylesheet">
<style>
  :root {
    --backdrop: #e4e4e4;
    --ink: #111111;
    --paper: #ffffff;
    --grey-light: #9a9a9a;
    --grey-mid: #6e6e6e;
    --grey-dark: #5a5a5a;
    --tagline: #8a8a8a;
  }
  * { margin: 0; padding: 0; box-sizing: border-box; }
  html, body {
    width: 1200px; height: 1000px; overflow: hidden;
    background: var(--backdrop);
  }
  .board { position: relative; width: 1200px; height: 1000px; }

  .card {
    position: absolute;
    width: 540px; height: 340px;
    overflow: hidden;
    box-shadow: 0 6px 18px rgba(0,0,0,0.18);
  }
  .card--dark { left: 60px; top: 130px; background: var(--ink); color: var(--paper); }
  .card--light { left: 600px; top: 530px; background: var(--paper); color: var(--ink); }

  .guitar-art {
    position: absolute;
    right: -60px; top: -40px;
    width: 290px; height: 250px;
    border-radius: 48% 40% 50% 46%;
    background: radial-gradient(circle at 55% 60%, var(--grey-dark) 0%, var(--grey-mid) 55%, var(--grey-light) 100%);
  }

  .tagline {
    position: absolute; left: 30px; top: 52px;
    font-family: "Questrial", sans-serif;
    font-size: 22px; letter-spacing: 0.5px;
    color: var(--tagline);
    word-spacing: 10px;
  }
  .name {
    position: absolute; left: 30px; top: 96px;
    font-family: "Archivo Black", sans-serif;
    font-size: 44px; letter-spacing: 0.5px;
    line-height: 1;
  }
  .contacts {
    position: absolute; left: 30px; top: 200px;
    list-style: none;
    font-family: "Questrial", sans-serif;
    font-size: 17px; font-weight: 700;
  }
  .contacts li {
    display: flex; align-items: center; gap: 10px;
    height: 27px;
  }
  .contacts svg { width: 16px; height: 16px; flex: none; }
  .icon-fill { fill: var(--grey-light); }
  .icon-line { fill: none; stroke: var(--grey-light); stroke-width: 1.6; }
</style>
</head>
<body>
<main class="board">

  <section class="card card--dark">
    <div class="guitar-art" role="img" aria-label="Abstrakte Grafik einer klassischen Gitarre in Grautönen"></div>
    <p class="tagline">Gitarrenlehrer Komponist Arrangeur</p>
    <h1 class="name">TOMAS MARENKO</h1>
    <ul class="contacts">
      <li><svg viewBox="0 0 16 16"><path class="icon-fill" d="M3 1.5l2.5 0 1 3.5-1.6 1.2a8 8 0 0 0 4.9 4.9l1.2-1.6 3.5 1v2.5c0 .8-.7 1.5-1.5 1.5A12 12 0 0 1 1.5 3C1.5 2.2 2.2 1.5 3 1.5z"/></svg>+49 170 555 123 45</li>
      <li><svg viewBox="0 0 16 16"><circle class="icon-fill" cx="8" cy="8" r="7.5"/><path d="M4 5.5h8v5H4z M4 5.5l4 3 4-3" fill="none" stroke="#222" stroke-width="1"/></svg>tomas@saitenklang.de</li>
      <li><svg viewBox="0 0 16 16"><circle class="icon-fill" cx="8" cy="8" r="7.5"/><circle cx="8" cy="8" r="4" fill="none" stroke="#222" stroke-width="1"/><path d="M4 8h8M8 4c-2 2.5-2 5.5 0 8M8 4c2 2.5 2 5.5 0 8" fill="none" stroke="#222" stroke-width="1"/></svg>www.saitenklang.de</li>
      <li><svg viewBox="0 0 16 16"><rect class="icon-line" x="1.5" y="1.5" width="13" height="13" rx="3"/><path class="icon-line" d="M5 5l6 6M11 5l-6 6"/></svg>Lindenweg 7, München 80331</li>
    </ul>
  </section>

  <section class="card card--light">
    <div class="guitar-art" role="img" aria-label="Abstrakte Grafik einer klassischen Gitarre in Grautönen"></div>
    <p class="tagline">Gitarrenlehrer Komponist Arrangeur</p>
    <h2 class="name">TOMAS MARENKO</h2>
    <ul class="contacts">
      <li><svg viewBox="0 0 16 16"><path class="icon-fill" d="M3 1.5l2.5 0 1 3.5-1.6 1.2a8 8 0 0 0 4.9 4.9l1.2-1.6 3.5 1v2.5c0 .8-.7 1.5-1.5 1.5A12 12 0 0 1 1.5 3C1.5 2.2 2.2 1.5 3 1.5z"/></svg>+49 170 555 123 45</li>
      <li><svg viewBox="0 0 16 16"><circle class="icon-fill" cx="8" cy="8" r="7.5"/><path d="M4 5.5h8v5H4z M4 5.5l4 3 4-3" fill="none" stroke="#fff" stroke-width="1"/></svg>tomas@saitenklang.de</li>
      <li><svg viewBox="0 0 16 16"><circle class="icon-fill" cx="8" cy="8" r="7.5"/><circle cx="8" cy="8" r="4" fill="none" stroke="#fff" stroke-width="1"/><path d="M4 8h8M8 4c-2 2.5-2 5.5 0 8M8 4c2 2.5 2 5.5 0 8" fill="none" stroke="#fff" stroke-width="1"/></svg>www.saitenklang.de</li>
      <li><svg viewBox="0 0 16 16"><rect class="icon-line" x="1.5" y="1.5" width="13" height="13" rx="3"/><path class="icon-line" d="M5 5l6 6M11 5l-6 6"/></svg>Lindenweg 7, München 80331</li>
    </ul>
  </section>

</main>
</body>
</html>
```